Create an awesome website for a medical clinic

This is a new website for a doctor's office. The site should be clean and modern, easy to navigate.

This is a wellness clinic, we want to help our clients have a healthy, active lifestyle. It should be friendly and inviting, and easy for them to call or schedule an appointment.

The site should be responsive and designed using the attached Bootstrap 3 PSD.

We will provide stock photos, until then please use stock photos from:

pictovault.net or
imagebarrow.net (preferred)

Some example sites of clean and modern designs that we like:

https://tarvelspine.example/
http://quellmarrow.example/
http://brisklyhale.example/

Also attached is a temporary logo you can use.

Reason: Thank you everyone for your great designs - we need a little more time so I'm extending the project.

Need extra days to review

Also, the colors in the new logo I just linked to are the final colors of the logo, so feel free to use any complimentary colors to it.

Hi everyone, The boss wants to change the layout of the site a little bit - here's the revised layout: https://www.filecrate.example/s/k9pz31xq7vn84te/notes%2011_29_2017.pdf?dl=0 And the graphic assets you can use are here: https://www.filecrate.example/s/k9pz31xq7vn84te/notes%2011_29_2017.pdf?dl=0 Feel free to change the background color of the "topbar", and change the icons of the "why people trust us" if you want, these are just temporary placeholders. Thanks for your patience and hard work!

Target Market(s)

People seeking medical treatment (wellness clinic)

Industry/Entity Type

Doctor

Number of Pages Required

1 page

Font styles to use
Sans Serif

Colors
0592cd
33a6d7
abd037
9bcb3c

Requirements
Must have
• The home page should have: a strong hero image/slideshow, clinic phone number should be prominent and at the top of the page (in the nav), a "what to expect" section (this is like a FAQs section - see attachment), and a strong call to action (a button to call or schedule an appointment).
• The what to expect section is useful so that prospective clients can determine if we're a good fit for them or not. It's a basic, first-step pre-qualification block of information.
• Social media icons which links to our social media profiles should be included.
Nice to have
• - Link to 3 most recent blog entries
• - Testimonials
• - How a multilevel nav menu looks.

```html
<!DOCTYPE html>
<html lang="en">
<head>
<meta charset="utf-8">
<title>Fernvale Medical Clinic</title>
<link rel="stylesheet" href="https://fonts.googleapis.com/css2?family=Montserrat:wght@400;600;700&family=Open+Sans:wght@400;600;700&display=swap">
<style>
:root{
  --blue:#0592cd;
  --blue-light:#33a6d7;
  --blue-dark:#1f7fc2;
  --green:#9bcb3c;
  --green-bright:#abd037;
  --gray-bg:#ececec;
  --text:#333;
  --muted:#555;
  --white:#fff;
  --line:#d9d9d9;
}
*{box-sizing:border-box;margin:0;padding:0}
html,body{width:1200px;height:3896px;overflow:hidden}
body{position:relative;font-family:"Open Sans",Arial,sans-serif;color:var(--text);background:var(--white)}
.abs{position:absolute}
.head-font{font-family:"Montserrat",Arial,sans-serif}
.btn{position:absolute;display:flex;align-items:center;justify-content:center;font-family:"Montserrat",Arial,sans-serif;font-weight:700;color:var(--white);text-transform:uppercase;letter-spacing:.5px}
.btn-blue{background:var(--blue)}
.btn-green{background:var(--green)}
.section{position:absolute;left:0;width:1200px}
.section-title{position:absolute;left:0;width:1200px;text-align:center;font-family:"Montserrat",Arial,sans-serif;font-weight:700;font-size:27px;text-transform:uppercase;letter-spacing:.5px}
.title-rule{position:absolute;left:567px;width:66px;height:4px}

/* header */
.site-header{top:0;height:117px;background:var(--white)}
.logo{position:absolute;left:143px;top:14px;font-family:"Montserrat",Arial,sans-serif;font-weight:700;color:var(--green);line-height:1}
.logo .l1{font-size:44px;letter-spacing:.5px}
.logo .l2{font-size:21px;margin-top:3px}
.follow{position:absolute;left:704px;top:28px;font-size:10px;font-weight:700;font-family:"Montserrat",sans-serif;color:var(--text)}
.social{position:absolute;width:24px;height:24px;border-radius:50%}
.call-icon{position:absolute;left:878px;top:18px;width:32px;height:32px;border-radius:50%;background:var(--blue-dark)}
.call-label{position:absolute;left:925px;top:20px;font-size:9px;font-weight:700;font-family:"Montserrat",sans-serif}
.call-number{position:absolute;left:922px;top:30px;font-size:25px;font-weight:700;font-family:"Montserrat",sans-serif;color:var(--green)}
.main-nav{position:absolute;left:520px;top:68px;display:flex;gap:6px;font-family:"Montserrat",sans-serif;font-size:12px;font-weight:700;text-transform:uppercase}
.main-nav a{color:var(--text);text-decoration:none;padding:6px 9px}
.main-nav a.active{background:var(--green);color:var(--white)}

/* hero */
.hero{top:117px;height:545px}
.hero-photo{position:absolute;inset:0;background:radial-gradient(ellipse at 60% 35%,#fffbe9 0%,#fbe7a3 30%,#f3b64a 62%,#d37a18 100%)}
.hero-title{position:absolute;left:267px;top:128px;font-family:"Montserrat",Arial,sans-serif;font-weight:600;font-size:50px;line-height:58px;color:var(--blue-dark)}
.hero .btn{left:270px;top:273px;width:283px;height:40px;font-size:15px}
.dots{position:absolute;left:555px;top:504px;display:flex;gap:13px}
.dots span{width:8px;height:8px;border-radius:50%;background:rgba(255,255,255,.8)}
.dots span.on{background:var(--blue-dark)}

/* welcome */
.welcome{top:662px;height:421px}
.welcome .kicker{position:absolute;left:143px;top:86px;font-family:"Montserrat",sans-serif;font-weight:700;font-size:15px}
.welcome h2{position:absolute;left:143px;top:108px;font-family:"Montserrat",sans-serif;font-weight:700;font-size:27px;color:var(--green)}
.body-copy{position:absolute;font-size:13.5px;line-height:22px;color:var(--muted)}
.welcome .body-copy{left:143px;top:160px;width:430px}
.welcome .btn{left:143px;top:291px;width:130px;height:37px;font-size:13px}
.video{position:absolute;left:610px;top:63px;width:447px;height:293px;background:linear-gradient(180deg,#9cc6ea 0%,#cfe3f1 48%,#7fae45 60%,#4e8426 100%)}

/* services */
.services{top:1083px;height:558px;background:var(--blue)}
.services .section-title{top:40px;color:var(--white)}
.services .title-rule{top:86px;background:var(--green)}
.service{position:absolute;top:145px;width:288px;text-align:center;color:var(--white)}
.service .photo{height:234px}
.service h3{margin-top:30px;font-family:"Montserrat",sans-serif;font-size:14px;font-weight:700;text-transform:uppercase}
.service p{margin:10px auto 0;width:200px;font-size:11.5px;line-height:16px}
.service .btn{position:relative;margin:12px auto 0;width:88px;height:22px;font-size:10px;color:#2a3b08}

/* clinic */
.clinic{top:1641px;height:504px;background:var(--gray-bg)}
.clinic-photo{position:absolute;left:145px;top:60px;width:546px;height:377px;background:linear-gradient(135deg,#f4f4f4 0%,#dfe2e4 55%,#c2c8cc 100%)}
.clinic h2{position:absolute;left:743px;top:70px;font-family:"Montserrat",sans-serif;font-weight:700;font-size:27px;color:var(--green)}
.clinic .title-rule{left:745px;top:106px;background:var(--blue)}
.clinic .body-copy{left:745px;top:147px;width:315px;text-align:justify}
.clinic .btn{left:745px;top:330px;width:130px;height:37px;font-size:13px}

/* blog */
.blog{top:2145px;height:574px}
.blog .section-title{top:60px;color:var(--green)}
.blog .title-rule{top:104px;background:var(--blue)}
.post{position:absolute;top:158px;width:302px;height:343px;border:1px solid var(--line);padding:10px}
.post .photo{height:200px}
.post p{margin-top:14px;font-size:13.5px;line-height:19px;color:var(--text);padding:0 6px}
.post .btn{left:22px;top:298px;width:104px;height:27px;font-size:11px}

/* testimonials */
.testimonials{top:2719px;height:390px;background:var(--green)}
.testimonials .section-title{top:55px;color:var(--white)}
.testimonials .title-rule{top:96px;background:var(--white)}
.quote{position:absolute;left:377px;top:148px;width:454px;text-align:center;font-size:13.5px;line-height:26px;color:#2c3a10}
.quote-author{position:absolute;left:0;width:1200px;top:312px;text-align:center;font-family:"Montserrat",sans-serif;font-weight:700;font-size:12px;color:#2c3a10}
.testimonials svg{position:absolute}

/* expect */
.expect{top:3109px;height:462px}
.expect .section-title{top:60px;color:var(--green)}
.expect .title-rule{top:104px;background:var(--blue)}
.faq{position:absolute;top:158px;width:302px;height:236px;border:1px solid var(--line);padding:24px 24px}
.faq h3{font-size:14px;font-weight:700;line-height:20px;color:#222}
.faq p{margin-top:14px;font-size:13px;line-height:20px;color:var(--muted)}

/* footer */
.site-footer{top:3571px;height:325px;background:var(--blue)}
.footer-logo{position:absolute;left:143px;top:57px;font-family:"Montserrat",sans-serif;font-weight:700;color:var(--white);line-height:1}
.footer-logo .l1{font-size:44px}
.footer-logo .l2{font-size:21px;margin-top:3px}
.footer-col{position:absolute;top:57px;color:var(--white)}
.footer-col h4{font-family:"Montserrat",sans-serif;font-size:12px;font-weight:700;text-transform:uppercase}
.footer-menu{margin-top:20px;list-style:none;font-size:10.5px;line-height:18px;text-transform:uppercase}
.contact-row{position:relative;margin-top:14px;padding-left:32px;font-size:11.5px;line-height:17px}
.contact-row svg{position:absolute;left:6px;top:2px}
.footer-rule{position:absolute;left:143px;top:241px;width:914px;height:1px;background:rgba(255,255,255,.5)}
.copyright{position:absolute;left:0;width:1200px;top:280px;text-align:center;font-size:10.5px;color:var(--white)}
</style>
</head>
<body>

<header class="section site-header">
  <div class="logo"><div class="l1">FERNVALE</div><div class="l2">MEDICAL CLINIC</div></div>
  <div class="follow">FOLLOW US</div>
  <span class="social" style="left:771px;top:22px;background:var(--blue-dark)"></span>
  <span class="social" style="left:798px;top:22px;background:var(--blue-light)"></span>
  <span class="social" style="left:825px;top:22px;background:#1b4f8a"></span>
  <span class="call-icon"><svg width="32" height="32" viewBox="0 0 32 32"><path d="M11 9c1 0 2 3 2 4s-2 1-1 3 3 4 4 4 1-2 3-1 4 1 4 2-2 3-4 3c-5 0-11-6-11-11 0-2 2-4 3-4z" fill="#fff"/></svg></span>
  <div class="call-label">CALL US</div>
  <div class="call-number">888.888.8888</div>
  <nav class="main-nav">
    <a class="active">Home</a><a>About Us</a><a>Services</a><a>Clinic</a><a>Blog</a><a>Testimonials</a><a>Contact Us</a>
  </nav>
</header>

<section class="section hero">
  <div class="hero-photo" role="img" aria-label="Woman in white with arms outstretched in a sunlit golden field"></div>
  <h1 class="hero-title">Best Health<br>Services</h1>
  <a class="btn btn-green">Schedule an appointment</a>
  <div class="dots"><span></span><span></span><span class="on"></span><span></span><span></span></div>
</section>

<section class="section welcome">
  <div class="kicker">WELCOME TO</div>
  <h2>FERNVALE MEDICAL CLINIC</h2>
  <p class="body-copy">There are many variations of passages of Lorem Ipsum available, but the majority have suffered alteration in some form, by injected humour, or randomised words which don't look even slightly believable. If you are going to use a passage of Lorem Ipsum, you need to be sure there isn't anything embarrassing hidden in the middle of text.</p>
  <a class="btn btn-blue">Read more</a>
  <div class="video" role="img" aria-label="Video still: two people celebrating on a green hilltop under blue sky">
    <svg width="447" height="293" viewBox="0 0 447 293"><circle cx="223" cy="146" r="30" fill="none" stroke="#fff" stroke-width="5"/><path d="M213 130l24 16-24 16z" fill="#fff"/></svg>
  </div>
</section>

<section class="section services">
  <h2 class="section-title">Our Services</h2>
  <div class="title-rule"></div>
  <div class="service" style="left:143px">
    <div class="photo" role="img" aria-label="Couple relaxing at a spa with flowers" style="background:linear-gradient(135deg,#f3e3d0,#d9a77c 60%,#a8683f)"></div>
    <h3>Wellness Clinic</h3>
    <p>There are many variations of passages of Lorem Ipsum available.</p>
    <a class="btn btn-green">Read more</a>
  </div>
  <div class="service" style="left:457px">
    <div class="photo" role="img" aria-label="Woman leaping joyfully in a meadow" style="background:linear-gradient(180deg,#d9a7e0,#f2d8ef 45%,#c9e6a0 70%,#6fa83a)"></div>
    <h3>Healthy</h3>
    <p>There are many variations of passages of Lorem Ipsum available.</p>
    <a class="btn btn-green">Read more</a>
  </div>
  <div class="service" style="left:766px">
    <div class="photo" role="img" aria-label="Woman in a sun hat and striped top outdoors" style="background:linear-gradient(135deg,#e8d6be,#b99a7a 55%,#5c4b42)"></div>
    <h3>Active Lifestyle</h3>
    <p>There are many variations of passages of Lorem Ipsum available.</p>
    <a class="btn btn-green">Read more</a>
  </div>
</section>

<section class="section clinic">
  <div class="clinic-photo" role="img" aria-label="Collage of bright clinic treatment rooms with examination beds"></div>
  <h2>OUR CLINIC</h2>
  <div class="title-rule"></div>
  <p class="body-copy">There are many variations of passages of Lorem Ipsum available, but the majority have suffered alteration in some form, by injected humour, or randomised words which don't look even slightly believable. If you are going to use a passage of Lorem Ipsum, you need to be sure there isn't anything embarrassing hidden in the middle of text.</p>
  <a class="btn btn-blue">Read more</a>
</section>

<section class="section blog">
  <h2 class="section-title">Latest Blog</h2>
  <div class="title-rule"></div>
  <article class="post" style="left:130px">
    <div class="photo" role="img" aria-label="Dental treatment room with chair" style="background:linear-gradient(135deg,#eef3f3,#a9cfcb 55%,#3f8f8a)"></div>
    <p>Lorem Ipsum is simply dummy text of the printing and typesetting industry</p>
    <a class="btn btn-blue">Read more</a>
  </article>
  <article class="post" style="left:447px">
    <div class="photo" role="img" aria-label="Couple jogging along a path at sunset" style="background:linear-gradient(180deg,#f6d89a,#d9a54c 50%,#7c7a3a)"></div>
    <p>There are many variations of passages of Lorem Ipsum available, but the majority have suffered</p>
    <a class="btn btn-blue">Read more</a>
  </article>
  <article class="post" style="left:764px">
    <div class="photo" role="img" aria-label="Woman running on a mountain trail" style="background:linear-gradient(180deg,#b9d4ea,#e2ebef 35%,#8a9a6a 60%,#5f6b45)"></div>
    <p>All the Lorem Ipsum generators on the Internet tend to repeat predefined chunks as necessary</p>
    <a class="btn btn-blue">Read more</a>
  </article>
</section>

<section class="section testimonials">
  <h2 class="section-title">Testimonials</h2>
  <div class="title-rule"></div>
  <svg style="left:206px;top:190px" width="16" height="28" viewBox="0 0 16 28"><path d="M13 2L3 14l10 12" fill="none" stroke="#fff" stroke-width="3"/></svg>
  <svg style="left:938px;top:190px" width="16" height="28" viewBox="0 0 16 28"><path d="M3 2l10 12L3 26" fill="none" stroke="#fff" stroke-width="3"/></svg>
  <svg style="left:323px;top:128px" width="30" height="26" viewBox="0 0 30 26"><path d="M0 26V14C0 6 4 1 11 0v5c-4 1-5 4-5 8h5v13zM17 26V14c0-8 4-13 11-14v5c-4 1-5 4-5 8h5v13z" fill="#fff"/></svg>
  <svg style="left:744px;top:256px" width="30" height="26" viewBox="0 0 30 26"><path d="M30 0v12c0 8-4 13-11 14v-5c4-1 5-4 5-8h-5V0zM13 0v12c0 8-4 13-11 14v-5c4-1 5-4 5-8H2V0z" fill="#fff"/></svg>
  <p class="quote">There are many variations of passages of Lorem Ipsum available, but the majority have suffered alteration in some form, by injected humour, or randomised words which don't look even slightly believable. If you are going to use a passage of Lorem Ipsum, you need to be sure there isn't anything embarrassing hidden in the middle of text.</p>
  <div class="quote-author">MARLA QUENTIN</div>
</section>

<section class="section expect">
  <h2 class="section-title">What to Expect</h2>
  <div class="title-rule"></div>
  <div class="faq" style="left:130px">
    <h3>Lorem Ipsum is simply dummy text of the printing and typesetting?</h3>
    <p>If you are going to use a passage of Lorem Ipsum, you need to be sure there isn't anything embarrassing hidden in the middle of text. There are many variations of passages of Lorem Ipsum available, but the majority.</p>
  </div>
  <div class="faq" style="left:447px">
    <h3>It uses a dictionary of over 200 Latin words, combined with a handful</h3>
    <p>If you are going to use a passage of Lorem Ipsum, you need to be sure there isn't anything embarrassing hidden in the middle of text. There are many variations of passages of Lorem Ipsum available, but the majority.</p>
  </div>
  <div class="faq" style="left:764px">
    <h3>All the Lorem Ipsum generators on the Internet tend to repeat.</h3>
    <p>If you are going to use a passage of Lorem Ipsum, you need to be sure there isn't anything embarrassing hidden in the middle of text. There are many variations of passages of Lorem Ipsum available, but the majority.</p>
  </div>
</section>

<footer class="section site-footer">
  <div class="footer-logo"><div class="l1">FERNVALE</div><div class="l2">MEDICAL CLINIC</div></div>
  <div class="footer-col" style="left:441px">
    <h4>Menu</h4>
    <ul class="footer-menu"><li>Home</li><li>About Us</li><li>Services</li><li>Clinic</li><li>Blog</li><li>Testimonials</li><li>Contact Us</li></ul>
  </div>
  <div class="footer-col" style="left:628px">
    <h4>Contact Us</h4>
    <div class="contact-row" style="margin-top:22px"><svg width="10" height="14" viewBox="0 0 10 14"><path d="M5 0a5 5 0 0 1 5 5c0 4-5 9-5 9S0 9 0 5a5 5 0 0 1 5-5z" fill="#fff"/><circle cx="5" cy="5" r="2" fill="var(--blue)"/></svg>41 Harbor Lane, Linden<br>Bay, FL 30000</div>
    <div class="contact-row"><svg width="12" height="12" viewBox="0 0 12 12"><path d="M3 0c1 0 2 2 2 3s-1 1-.5 2 2 2.5 3 2.5 1-1 2-.5 2.5 1 2.5 2-1 2-3 2C5 11 1 7 1 3c0-1.5 1-3 2-3z" fill="#fff"/></svg>888 888 8888</div>
    <div class="contact-row"><svg width="13" height="10" viewBox="0 0 13 10"><rect width="13" height="10" fill="#fff"/><path d="M0 0l6.5 5L13 0" fill="none" stroke="var(--blue)" stroke-width="1.2"/></svg>info@fernvaleclinic.example</div>
  </div>
  <div class="footer-col" style="left:922px">
    <h4>Follow Us</h4>
    <span class="social" style="left:0;top:30px;width:38px;height:38px;background:#1b5aa8"></span>
    <span class="social" style="left:46px;top:30px;width:38px;height:38px;background:var(--blue-light)"></span>
    <span class="social" style="left:92px;top:30px;width:38px;height:38px;background:#153f78"></span>
  </div>
  <div class="footer-rule"></div>
  <div class="copyright">Copyright © 2017 All Rights Reserved</div>
</footer>

</body>
</html>
```